Bag packaging design of sliced bread

The project is for design of line of sliced bread with different flavours. The brand of the bread will be "Velorasa". The shape of the bread will be oval. The bread will be packed in a bag. I attach the layout of the bag. The bag will be closed with a plastic clip. I attach images of similar products. The idea is to have one main design and then each colour to be different type of bread like those in the images 2 and 5.

```html
<!DOCTYPE html>
<html lang="en">
<head>
<meta charset="utf-8">
<title>Velorasa Sliced Bread – Bag Layouts</title>
<link rel="stylesheet" href="https://fonts.googleapis.com/css2?family=Oswald:wght@400;600&display=swap">
<style>
  :root {
    --page-top: #fdf1df;
    --page-bottom: #fffdfa;
    --white: #ffffff;
    --wheat-light: #f6d48a;
    --wheat-deep: #c98a2e;

    --orange-body: #ff9c00;
    --orange-dark: #4a2508;
    --orange-accent: #ff9c00;

    --green-body: #99cc00;
    --green-dark: #0b6b0b;
    --green-accent: #99cc00;

    --pink-body: #ff9ea1;
    --pink-dark: #c8142d;
    --pink-accent: #ffa9ab;
  }
  html, body {
    margin: 0;
    width: 780px;
    height: 1200px;
    overflow: hidden;
  }
  body {
    background: linear-gradient(180deg, var(--page-top), var(--page-bottom));
    font-family: "Oswald", sans-serif;
  }
  .dielines {
    position: absolute;
    left: 0;
    top: 335px;
    width: 780px;
    height: 530px;
  }
  .variant-orange { --body: var(--orange-body); --dark: var(--orange-dark); --accent: var(--orange-accent); }
  .variant-green  { --body: var(--green-body);  --dark: var(--green-dark);  --accent: var(--green-accent); }
  .variant-pink   { --body: var(--pink-body);   --dark: var(--pink-dark);   --accent: var(--pink-accent); }

  .bag-body { fill: var(--body); }
  .bag-rule { fill: var(--dark); }
  .bag-band { fill: var(--dark); }
  .band-name { fill: var(--accent); font-family: "Oswald", sans-serif; font-weight: 600; font-size: 19px; letter-spacing: 1px; }
  .badge-frame { fill: var(--dark); }
  .badge-inner-line { fill: var(--accent); }
  .badge-face { fill: var(--white); }
  .badge-rule { stroke: var(--accent); stroke-width: 2.5; }
  .claim-big { fill: var(--accent); font-family: "Oswald", sans-serif; font-weight: 600; font-size: 22px; }
  .claim-small { fill: var(--dark); font-family: "Oswald", sans-serif; font-weight: 400; font-size: 9px; letter-spacing: .5px; }
  .brand-name { fill: var(--dark); font-family: "Oswald", sans-serif; font-weight: 600; font-size: 34px; letter-spacing: 1px; }
  .flavour { fill: var(--dark); font-family: "Oswald", sans-serif; font-weight: 600; font-size: 34px; }
  .weight { fill: var(--accent); font-family: "Oswald", sans-serif; font-weight: 600; font-size: 20px; }
</style>
</head>
<body>
<svg class="dielines" viewBox="34 1298 1476 1002" xmlns="http://www.w3.org/2000/svg">
  <defs>
    <linearGradient id="wheat-tone" x1="0" y1="1" x2="1" y2="0">
      <stop offset="0" stop-color="var(--wheat-deep)"/>
      <stop offset="1" stop-color="var(--wheat-light)"/>
    </linearGradient>
    <g id="bag-layout">
      <!-- front panel -->
      <rect class="bag-band" x="0" y="0" width="443" height="62"/>
      <rect class="bag-body" x="0" y="42" width="443" height="13"/>
      <rect class="bag-body" x="0" y="62" width="443" height="358" role="img" aria-label="Bag surface with a faint wheat-ear pattern"/>
      <rect class="bag-rule" x="0" y="400" width="443" height="8"/>
      <text class="band-name" x="78" y="28" text-anchor="middle">Velorasa</text>
      <text class="band-name" x="222" y="28" text-anchor="middle">Velorasa</text>
      <text class="band-name" x="366" y="28" text-anchor="middle">Velorasa</text>

      <!-- label badge -->
      <polygon class="badge-frame" points="121,327 314,327 314,607 218,698 121,607"/>
      <polygon class="badge-inner-line" points="127,333 308,333 308,604 218,689 127,604"/>
      <polygon class="badge-face" points="131,337 304,337 304,602 218,683 131,602"/>
      <rect x="215" y="337" width="88" height="72" fill="url(#wheat-tone)" role="img" aria-label="Golden wheat ears illustration"/>
      <text class="claim-big" x="145" y="378">100%</text>
      <text class="claim-small" x="146" y="391">NATURALA</text>
      <text class="brand-name" x="218" y="474" text-anchor="middle">Velorasa</text>
      <line class="badge-rule" x1="146" y1="524" x2="290" y2="524"/>
      <text class="flavour" x="218" y="560" text-anchor="middle">WHOLE</text>
      <text class="flavour" x="218" y="594" text-anchor="middle">WHEAT</text>
      <line class="badge-rule" x1="146" y1="608" x2="290" y2="608"/>
      <text class="weight" x="218" y="645" text-anchor="middle">500gr</text>

      <!-- back panel -->
      <rect class="bag-body" x="0" y="755" width="443" height="247" role="img" aria-label="Bag back surface with a faint wheat-ear pattern"/>
      <rect class="bag-rule" x="0" y="762" width="443" height="8"/>
    </g>
  </defs>
  <use href="#bag-layout" class="variant-orange" x="34" y="1298"/>
  <use href="#bag-layout" class="variant-green" x="559" y="1298"/>
  <use href="#bag-layout" class="variant-pink" x="1067" y="1298"/>
</svg>
</body>
</html>
```